New Branding Business Card Design

Redesign business card according to new branding update.

** The design received so far are single color + BLACK.
I'd encourage designer to use different tones of blue / purple as described in the Designer Brief color palette

Target Market(s)

International

Industry/Entity Type

Medical Equipment

Contact Information for Business Card

Logo on one side (Designer can decide if they want to move certain info from the other side to save space)

Main body info (company name, individual name in both English and Chinese, contact info etc) on the other
Prefer a 'cleaner' layout - vs 'all over the place'
Prefer flush left alignment

Font styles to use
Sans Serif

Requirements
Must have
• Key info
• (Company name (English)): VORAM (HK) Limited
• (Name (English)): Marcus L. Pryde
• (Credential): FCPA, FHKSI
• (Title): Founder, Managing Director & CEO
• For the following info, designers decide whether to use colon or no colon, stroke separator, or use icon gfx for T (for telephone fixed line, M for mobile etc.)
• T: +852 3517 VORAM / +852 3517 4062
• M: +852 6243 7719 / + 86 139 2745 3186
• E: marcus.l.pryde@voram-example.hk
Nice to have
• Depending on the space and spacing available designers can add or use fuller title and other info
• Title: Chairman of the Executive Committee, Founder, Managing Director & CEO
• (Name (Chinese)): 林書恒
Should not have
• One of our business entities a long company name that cannot be broken into 2 lines
• makes vertical implementation almost impossible

```html
<!DOCTYPE html>
<html lang="en">
<head>
<meta charset="utf-8">
<title>VORAM business card</title>
<link rel="stylesheet" href="https://fonts.googleapis.com/css2?family=Open+Sans:wght@400;600;700&family=Noto+Sans+TC:wght@400&display=swap">
<style>
  :root {
    --backdrop: #34302d;
    --card: #0e0e0f;
    --purple: #7a3fae;
    --text-light: #e6e6e6;
    --divider: #262628;
    --silver: #c9c9cb;
  }
  * { margin: 0; padding: 0; box-sizing: border-box; }
  html, body {
    width: 1200px; height: 844px; overflow: hidden;
    background: var(--backdrop);
    font-family: "Open Sans", Arial, sans-serif;
  }
  .stage {
    position: relative; width: 1200px; height: 844px;
    display: flex; align-items: center; justify-content: center; gap: 40px;
  }
  .card {
    width: 520px; height: 312px;
    background: var(--card);
    border-radius: 3px;
    position: relative;
    box-shadow: 0 10px 30px rgba(0,0,0,.35);
  }
  /* info side */
  .brand-panel {
    position: absolute; left: 0; top: 0; bottom: 0; width: 210px;
    display: flex; align-items: center; justify-content: center; gap: 10px;
    padding-top: 70px;
  }
  .brand-square { width: 18px; height: 18px; background: var(--purple); border-radius: 3px; }
  .brand-name { color: var(--purple); font-weight: 700; font-size: 34px; letter-spacing: 1px; }
  .divider {
    position: absolute; left: 212px; top: 24px; bottom: 24px;
    width: 1px; background: var(--divider);
  }
  .details { position: absolute; left: 232px; top: 34px; right: 16px; }
  .person-name {
    color: var(--purple); font-weight: 700; font-size: 15px;
    text-transform: uppercase; line-height: 1.2;
  }
  .credentials { font-size: 12px; font-weight: 600; }
  .person-name-zh {
    font-family: "Noto Sans TC", "Open Sans", sans-serif;
    color: var(--purple); font-size: 22px; line-height: 1.3;
  }
  .titles { color: var(--text-light); font-size: 14px; line-height: 1.3; margin-top: 6px; }
  .contacts { list-style: none; margin-top: 14px; }
  .contacts li {
    color: var(--text-light); font-size: 14px; line-height: 19px;
    display: flex; align-items: center; gap: 8px;
  }
  .contacts svg { width: 12px; height: 12px; flex: none; fill: var(--purple); }
  /* logo side */
  .logo-side { display: flex; align-items: center; justify-content: center; gap: 12px; }
  .logo-side .brand-square { background: var(--silver); width: 20px; height: 20px; }
  .logo-side .brand-name { color: var(--silver); font-size: 40px; }
</style>
</head>
<body>
<main class="stage">
  <section class="card info-side">
    <div class="brand-panel">
      <span class="brand-square"></span>
      <span class="brand-name">VORAM</span>
    </div>
    <div class="divider"></div>
    <div class="details">
      <p class="person-name">Marcus L. Pryde <span class="credentials">FCPA, FHKSI</span></p>
      <p class="person-name-zh">林書恒</p>
      <p class="titles">Founder<br>Managing Director &amp; CEO</p>
      <ul class="contacts">
        <li><svg viewBox="0 0 12 12"><path d="M1 4c0-2 2-3 5-3s5 1 5 3l-2 1-1-1H4L3 5zM2 6h8l1 5H1z"/></svg>+852 3517 VORAM</li>
        <li><svg viewBox="0 0 12 12"><path d="M1 4c0-2 2-3 5-3s5 1 5 3l-2 1-1-1H4L3 5zM2 6h8l1 5H1z"/></svg>+852 3517 4062</li>
        <li><svg viewBox="0 0 12 12"><path d="M3 0h6a1 1 0 0 1 1 1v10a1 1 0 0 1-1 1H3a1 1 0 0 1-1-1V1a1 1 0 0 1 1-1zm0 2v7h6V2z"/></svg>+852 6243 7719</li>
        <li><svg viewBox="0 0 12 12"><path d="M3 0h6a1 1 0 0 1 1 1v10a1 1 0 0 1-1 1H3a1 1 0 0 1-1-1V1a1 1 0 0 1 1-1zm0 2v7h6V2z"/></svg>+ 86 139 2745 3186</li>
        <li><svg viewBox="0 0 12 12"><path d="M0 2h12v8H0zm1 1v.5l5 3 5-3V3z"/></svg>marcus.l.pryde@voram-example.hk</li>
      </ul>
    </div>
  </section>
  <section class="card logo-side">
    <span class="brand-square"></span>
    <span class="brand-name">VORAM</span>
  </section>
</main>
</body>
</html>
```